Prepared Meal Company Needs Menu Design

We are a pre-prepared meal delivery company called Grubb Larderly.

We have a menu in excel but needs to be designed to look good and appealing to customers. The menu should be clean, easy to ready, and show:Title (Pupusa)Tags (V, V+, GF - Use a cool vegan logo for the V+ and logo for vegetarian V symbol)Price (12.99)DescriptionBrand colors are orange white and green. Design is clean, crisp and can incorporate natural elements like leaf shaped symbols, etc. Screenshots from our website attached for inspiration.

Target Market(s)

Broad demographics

Industry/Entity Type

Restaurant

Font styles to use
Sans Serif

Requirements
Must have
• The menu design should be commensurate with the website under development
• https://grubblarderly.dishsite.example
Nice to have
• Should have appropriate graphics
Should not have
• Modifiers do not need to be shown (these are shown in the excel only).

```html
<!DOCTYPE html>
<html lang="en">
<head>
<meta charset="utf-8">
<title>Grubb Larderly Menu</title>
<link href="https://fonts.googleapis.com/css2?family=Exo+2:wght@500;600&family=Mulish:ital,wght@0,600;0,700;1,400&display=swap" rel="stylesheet">
<style>
:root{
  --green:#1f8a3c;
  --green-dark:#16702f;
  --orange:#f07a1a;
  --paper:#fbf8f3;
  --watermark:#f3e8dc;
  --ink:#3d3d3d;
  --rule:#6a6a6a;
  --bg:#ffffff;
}
*{margin:0;padding:0;box-sizing:border-box}
html,body{width:1200px;height:729px;overflow:hidden;background:var(--bg)}
.canvas{position:relative;width:1200px;height:729px}
.page{position:absolute;top:25px;width:558px;height:675px;background:var(--paper);box-shadow:0 1px 5px rgba(0,0,0,.18);overflow:hidden}
.page--left{left:31px}
.page--right{left:612px;width:556px}
.page__band{position:absolute;left:0;right:0;bottom:0;height:12px;background:var(--green)}
.page__watermark{position:absolute;border-radius:50%;background:var(--watermark);opacity:.7}
.brand{position:absolute;top:14px;right:14px;width:74px;text-align:center}
.brand__dot{display:block;width:52px;height:52px;margin:0 auto 3px;border-radius:50%;background:var(--orange)}
.brand__name{font:700 9px/1 "Mulish",sans-serif;color:var(--orange)}
.section-tab{position:absolute;left:0;height:21px;width:126px;background:var(--orange);color:#fff;font:700 12.5px/21px "Mulish",sans-serif;padding-left:23px;clip-path:polygon(0 0,88% 0,100% 50%,88% 100%,0 100%)}
.item{position:absolute;left:54px;width:440px}
.page--right .item{left:53px}
.item__title{font:500 12.5px/14.5px "Exo 2",sans-serif;letter-spacing:.2px;color:var(--green);width:270px}
.item__desc{font:italic 400 7.3px/9.2px "Mulish",sans-serif;color:var(--ink);margin-left:19px;width:200px}
.item__tags{position:absolute;top:3.5px;left:274px;display:flex;gap:5px;align-items:center}
.page--right .item__tags{left:273px}
.item__tags--single{left:301px}
.page--right .item__tags--single{left:301px}
.item__tags svg{width:22px;height:22px;display:block}
.item__note{font:600 7px/1 "Mulish",sans-serif;color:#333;margin-left:-1px}
.item__extra{position:absolute;left:274px;top:27px;display:flex;gap:5px;align-items:center}
.item__extra svg{width:22px;height:22px;display:block}
.item__price{position:absolute;top:6.5px;right:0;font:600 10px/12px "Mulish",sans-serif;color:#333}
.rule{position:absolute;left:54px;width:436px;border-top:1px dashed var(--rule)}
</style>
</head>
<body>
<svg width="0" height="0" style="position:absolute" aria-hidden="true">
  <defs>
    <symbol id="tag-vegan" viewBox="0 0 24 24">
      <circle cx="12" cy="12" r="11.5" fill="#1f8a3c"/>
      <circle cx="12" cy="12" r="9" fill="none" stroke="#fff" stroke-width=".6"/>
      <text x="12" y="13.8" text-anchor="middle" font-family="Mulish,sans-serif" font-weight="700" font-size="5" fill="#fff">VEGAN</text>
    </symbol>
    <symbol id="tag-veg" viewBox="0 0 24 24">
      <circle cx="12" cy="12" r="11.5" fill="#1f8a3c"/>
      <circle cx="12" cy="12" r="8.5" fill="#fff"/>
      <path d="M7.5 7.5 L12 17 L16.5 7.5" fill="none" stroke="#1f8a3c" stroke-width="2.4" stroke-linejoin="round"/>
    </symbol>
    <symbol id="tag-gf" viewBox="0 0 24 24">
      <circle cx="12" cy="12" r="10.8" fill="#fff" stroke="#1f8a3c" stroke-width="1.6"/>
      <path d="M12 5 V19" stroke="#1f8a3c" stroke-width="1.4"/>
      <path d="M12 8 l-2.6 -1.6 M12 8 l2.6 -1.6 M12 11 l-2.6 -1.6 M12 11 l2.6 -1.6 M12 14 l-2.6 -1.6 M12 14 l2.6 -1.6" stroke="#1f8a3c" stroke-width="1.6" stroke-linecap="round"/>
      <path d="M5 5 L19 19" stroke="#1f8a3c" stroke-width="1.8"/>
    </symbol>
    <symbol id="tag-df" viewBox="0 0 24 24">
      <circle cx="12" cy="12" r="10.8" fill="#fff" stroke="#1f8a3c" stroke-width="1.6"/>
      <path d="M10 5.5 h4 v2.5 l1.5 2 v8.5 h-7 v-8.5 l1.5 -2 z" fill="#1f8a3c"/>
      <path d="M5 5 L19 19" stroke="#fff" stroke-width="3"/>
      <path d="M5 5 L19 19" stroke="#1f8a3c" stroke-width="1.6"/>
    </symbol>
  </defs>
</svg>

<main class="canvas">
  <section class="page page--left">
    <div class="page__watermark" aria-hidden="true" style="left:180px;top:210px;width:340px;height:340px"></div>
    <div class="brand"><span class="brand__dot"></span><span class="brand__name">Grubb Larderly</span></div>

    <div class="section-tab" style="top:59px">BREAKFAST</div>

    <div class="item" style="top:93.5px"><h3 class="item__title">Cinnamon-Apple Sunrise Oats</h3><p class="item__desc">Almond Milk &amp; Ceylon Cinnamon, Marinated Golden Raisins, Macca Powder, Apple-Pecan Crumble</p><div class="item__tags"><svg><use href="#tag-vegan"/></svg><svg><use href="#tag-gf"/></svg></div><span class="item__price">6.99</span></div>
    <div class="rule" style="top:134px"></div>

    <div class="item" style="top:143.5px"><h3 class="item__title">Acai Yogurt</h3><p class="item__desc">Coconut, Goji, Seasonal Fruit, Crunchy Chia Seeds, Ceylon Cinnamon</p><div class="item__tags"><svg><use href="#tag-veg"/></svg><svg><use href="#tag-gf"/></svg></div><span class="item__price">7.99</span></div>
    <div class="rule" style="top:186px"></div>

    <div class="item" style="top:196.5px"><h3 class="item__title">Millstone 7:3 Cereal &amp; Yogurt</h3><p class="item__desc">Apricot-Pear Compote, Almond &amp; Saba Drizzle</p><div class="item__tags"><svg><use href="#tag-veg"/></svg></div><span class="item__price">7.49</span></div>
    <div class="rule" style="top:231px"></div>

    <div class="item" style="top:240.5px"><h3 class="item__title">St. Benedict's Eggs</h3><p class="item__desc">2 Soft Yolk Eggs over Rosemary Polenta, Caramelized Onion, Mushrooms &amp; Asparagus, Lemon</p><div class="item__tags"><svg><use href="#tag-veg"/></svg><svg><use href="#tag-df"/></svg></div><span class="item__price">9.49</span></div>
    <div class="rule" style="top:282px"></div>

    <div class="item" style="top:290.5px"><h3 class="item__title">Pomegranate &amp; Saffron Shakshuka</h3><p class="item__desc">2 Soft Yolk Eggs over Roasted Tomatoes, Onions &amp; Peppers, Garden Herb Oil, Rosemary, Oregano &amp; Thyme with Handmade Gluten-Free Flatbread</p><div class="item__tags"><svg><use href="#tag-veg"/></svg><svg><use href="#tag-gf"/></svg><svg><use href="#tag-df"/></svg></div><span class="item__price">10.99</span></div>
    <div class="rule" style="top:342px"></div>

    <div class="item" style="top:351.5px"><h3 class="item__title">Sweet Potato Hash</h3><p class="item__desc">Broccolini, Cherry Tomato, Asparagus, Roasted Peppers &amp; Onions, Rosemary-Nutritional Yeast</p><div class="item__tags"><svg><use href="#tag-vegan"/></svg><svg><use href="#tag-gf"/></svg></div><span class="item__price">8.99</span></div>
    <div class="rule" style="top:394px"></div>

    <div class="item" style="top:402.5px"><h3 class="item__title">Mom's Frittata</h3><p class="item__desc">Roasted Cherry Tomato, Goat Cheese &amp; Baby Spinach with Sweet Potato Homefries</p><div class="item__tags"><svg><use href="#tag-veg"/></svg><svg><use href="#tag-gf"/></svg></div><span class="item__price">11.99</span></div>
    <div class="rule" style="top:446px"></div>

    <div class="item" style="top:456.5px"><h3 class="item__title">Country Style Breakfast Sandwich</h3><p class="item__desc">Arugula, Goat Cheese, Cherry Tomatoes &amp; Lemon with Mom's Frittata on Millstone 7:3 Bread</p><div class="item__tags"><svg><use href="#tag-veg"/></svg></div><span class="item__price">13.99</span></div>

    <div class="section-tab" style="top:510px">APPETIZERS</div>

    <div class="item" style="top:548.5px"><h3 class="item__title">Avocado Super-Toast</h3><p class="item__desc" style="width:215px">Shaved Fennel &amp; Golden Beets, Avocado, Garden Herb Oil, Lemon Juice, Ground Flax, Hemp Seed, Golden Raisin &amp; Moringa on Millstone 7:3 Sprouted Whole</p><div class="item__tags"><svg><use href="#tag-vegan"/></svg><svg><use href="#tag-gf"/></svg><span class="item__note">with Flatbread</span></div><span class="item__price">9.49</span></div>
    <div class="rule" style="top:600px"></div>

    <div class="item" style="top:608.5px"><h3 class="item__title">Pupusa</h3><p class="item__desc">Coconut, Goji, Seasonal Fruit, Crunchy Chia Seeds, Ceylon Cinnamon</p><div class="item__tags"><svg><use href="#tag-veg"/></svg><svg><use href="#tag-gf"/></svg></div><span class="item__price">9.49</span></div>

    <div class="page__band"></div>
  </section>

  <section class="page page--right">
    <div class="page__watermark" aria-hidden="true" style="left:170px;top:205px;width:340px;height:340px"></div>
    <div class="brand"><span class="brand__dot"></span><span class="brand__name">Grubb Larderly</span></div>

    <div class="item" style="top:81.5px"><h3 class="item__title">Pupusa Deluxe</h3><p class="item__desc">Sous Vide Bison Shortrib, Goat Cheese, Ayocote &amp; Avocado Puree, Nopales, Cilantro-Lime Yogurt, Inca Corn Crumble, Tropical Acai Hot Sauce</p><div class="item__tags item__tags--single"><svg><use href="#tag-gf"/></svg></div><span class="item__price">13.99</span></div>
    <div class="rule" style="top:130px"></div>

    <div class="item" style="top:137.5px"><h3 class="item__title">Egyptian Flatbread</h3><p class="item__desc">Honey-Chamomile Yogurt, Braised Cherry Tomatoes, Sumac &amp; Pistachio Dukkha, Garlic &amp; Micro Radish on Handmade Gluten-Free Flatbread</p><div class="item__tags"><svg><use href="#tag-veg"/></svg><svg><use href="#tag-gf"/></svg></div><span class="item__price">11.99</span></div>
    <div class="rule" style="top:186px"></div>

    <div class="item" style="top:191.5px"><h3 class="item__title">Green Street Tacos</h3><p class="item__desc">Sugar Snap Peas, Guacamole, Radish &amp; Inca Corn Crumble on 2 Handmade Corn Tortillas.</p><div class="item__tags"><svg><use href="#tag-vegan"/></svg><svg><use href="#tag-gf"/></svg></div><span class="item__price">9.99</span></div>
    <div class="rule" style="top:232px"></div>

    <div class="item" style="top:236.5px"><h3 class="item__title">Marinated Squash Tacos</h3><p class="item__desc" style="width:215px">Chayote Escabeche, Jalapeno, Guacamole, Carrots, Radish, Pepitas &amp; Cilantro, on 2 Handmade Corn Tortillas.</p><div class="item__tags"><svg><use href="#tag-veg"/></svg><svg><use href="#tag-gf"/></svg></div><span class="item__price">9.99</span></div>
    <div class="rule" style="top:276px"></div>

    <div class="item" style="top:285.5px"><h3 class="item__title" style="width:290px">Soft Yolk Egg &amp; Avocado "Toast" Flatbread</h3><p class="item__desc">Ayocote &amp; Avocado Puree, Guacamole, Sunflower Seeds, Inca Corn, Arugula, Lime &amp; Soft Yolk Egg on Handmade Gluten-Free Flatbread</p><div class="item__tags"><svg><use href="#tag-veg"/></svg><svg><use href="#tag-gf"/></svg></div><span class="item__price">10.99</span></div>

    <div class="section-tab" style="top:351px">SOUPS</div>

    <div class="item" style="top:390.5px"><h3 class="item__title">Seasonal Vegetable Minestrone<br>with Free Range Turkey Meatballs</h3><p class="item__desc">Ayocote Beans, Roasted Tomatoes, Carrots, Onions &amp; Bell Pepper, Snap Peas, Garnett Yam, Rosemary &amp; Oregano</p><div class="item__tags item__tags--single"><svg><use href="#tag-gf"/></svg></div><span class="item__price">9.49</span></div>
    <div class="rule" style="top:453px"></div>

    <div class="item" style="top:458.5px"><h3 class="item__title">Sweet Carrot &amp; Coriander Soup</h3><p class="item__desc">Garden Herb Oil, Cilantro, Toasted Pepita</p><div class="item__tags"><svg><use href="#tag-vegan"/></svg><svg><use href="#tag-gf"/></svg></div><span class="item__price">5.99</span></div>
    <div class="rule" style="top:492px"></div>

    <div class="item" style="top:500.5px"><h3 class="item__title">Butternut Squash &amp; Nopale Chili</h3><p class="item__desc" style="width:215px">Arugula, Goat Cheese, Cherry Tomatoes &amp; Lemon with Mom's Frittata on Millstone 7:3 Bread</p><div class="item__tags"><svg><use href="#tag-veg"/></svg><svg><use href="#tag-gf"/></svg></div><div class="item__extra"><svg><use href="#tag-vegan"/></svg><span class="item__note">if No Goat Cheese</span></div><span class="item__price" style="top:21.5px">13.99</span></div>
    <div class="rule" style="top:565px"></div>

    <div class="item" style="top:572.5px"><h3 class="item__title">Robert's Chicken Soup</h3><p class="item__desc" style="width:225px">Gluten-Free Sorghum Penne, Root Vegetables, Oregano &amp; Peppercorns on the Vine</p><div class="item__tags" style="left:301px"><svg><use href="#tag-gf"/></svg><svg><use href="#tag-df"/></svg></div><span class="item__price">5.99</span></div>

    <div class="page__band"></div>
  </section>
</main>
</body>
</html>
```